Homemaker goats milk soap label

The name of my farm is Fern N Heron Farm. I would like to keep my label vintage 1800s is appearance. A linked to my webpage, still under development is http://lopo.mivtrel.com/dev2/pastureway/. This will give you a feel for my theme. Along with other goat and bison by products, I make and sell homemade goat milk soap and I would like a special label to package my fabulous soap.
Updates

Hello Designers, To assist you with designing my label, I have attached a new photo from Lather Harbor that shows the type label I am going to use.

Industry/Entity Type

Farm

```html
<!DOCTYPE html>
<html lang="en">
<head>
<meta charset="utf-8">
<title>Fern N Heron Farm – Goat Milk Soap Label</title>
<link href="https://fonts.googleapis.com/css2?family=Rokkitt:wght@700;800&family=Pinyon+Script&family=Courier+Prime:wght@700&display=swap" rel="stylesheet">
<style>
  :root {
    --kraft-light: #eadbc2;
    --kraft-mid: #dcc6a3;
    --kraft-edge: #c6a57c;
    --ink-brown: #6e2b1b;
    --label-cream: #f1e6d2;
  }
  html, body {
    margin: 0;
    padding: 0;
    width: 1200px;
    height: 856px;
    overflow: hidden;
    background: var(--kraft-mid);
  }
  .soap-label {
    display: block;
    width: 1200px;
    height: 856px;
  }
  .label-rule { fill: var(--ink-brown); }
  .brand-mark { fill: var(--ink-brown); }
  .brand-name {
    font-family: "Rokkitt", serif;
    font-weight: 700;
    font-size: 62px;
    letter-spacing: 4px;
    fill: var(--ink-brown);
  }
  .tagline-natural {
    font-family: "Pinyon Script", cursive;
    font-size: 66px;
    fill: var(--ink-brown);
  }
  .product-title {
    font-family: "Rokkitt", serif;
    font-weight: 800;
    font-size: 128px;
    fill: var(--ink-brown);
  }
  .scent-box { fill: var(--ink-brown); }
  .scent-name {
    font-family: "Courier Prime", monospace;
    font-weight: 700;
    font-size: 60px;
    fill: var(--label-cream);
  }
  .net-weight {
    font-family: "Rokkitt", serif;
    font-weight: 800;
    font-size: 50px;
    fill: var(--ink-brown);
  }
</style>
</head>
<body>
<svg class="soap-label" viewBox="0 0 1200 856" xmlns="http://www.w3.org/2000/svg" role="img" aria-label="Fern N Heron Natural Home Crafted Goat Milk Soap, lavander, weight 4.25 to 4.5 oz">
  <defs>
    <radialGradient id="kraft-paper" cx="50%" cy="45%" r="70%">
      <stop offset="0%" stop-color="var(--kraft-light)"/>
      <stop offset="60%" stop-color="var(--kraft-mid)"/>
      <stop offset="100%" stop-color="var(--kraft-edge)"/>
    </radialGradient>
  </defs>

  <rect class="paper-background" width="1200" height="856" fill="url(#kraft-paper)"/>

  <!-- top border -->
  <rect class="label-rule" x="0" y="10" width="1200" height="10"/>
  <rect class="label-rule" x="0" y="31" width="1200" height="3"/>

  <!-- brand -->
  <circle class="brand-mark" cx="600" cy="110" r="64"/>
  <text class="brand-name" x="600" y="248" text-anchor="middle">FERN N HERON</text>

  <text class="tagline-natural" x="600" y="372" text-anchor="middle">Natural</text>

  <text class="product-title" x="600" y="496" text-anchor="middle" textLength="608" lengthAdjust="spacingAndGlyphs">Home Crafted</text>
  <text class="product-title" x="600" y="606" text-anchor="middle" textLength="666" lengthAdjust="spacingAndGlyphs">Goat Milk Soap</text>

  <!-- scent -->
  <rect class="scent-box" x="360" y="661" width="495" height="90"/>
  <text class="scent-name" x="609" y="722" text-anchor="middle" textLength="372" lengthAdjust="spacingAndGlyphs">lavander</text>

  <!-- weight -->
  <text class="net-weight" x="1030" y="706" text-anchor="middle" textLength="180" lengthAdjust="spacingAndGlyphs">Wt 4,25</text>
  <text class="net-weight" x="1050" y="766" text-anchor="middle" textLength="136" lengthAdjust="spacingAndGlyphs">-4,5oz</text>

  <!-- bottom border -->
  <rect class="label-rule" x="0" y="814" width="1200" height="3"/>
  <rect class="label-rule" x="0" y="832" width="1200" height="10"/>
</svg>
</body>
</html>
```